non prof needs power point design template

The Calmora Trust is a non profit financing and services organization. We are looking for creative ppt templates for various presentations. Including general org overview. marketing and ad decks, etc... Please utilize logo for inspiration for template. We like to communicate to our partners that we are a "business evolved" to served social causes and the public good.
We are launching next year. As such we do not have any other materials. I''m hoping you can provide a creative feel. Yes we''d like a cover page. Several slide templates for different content. Bullet points, graphs, charts, maps, statistics, combos, org charts, flow charts etc...
we work in the following sectors Agriculture and Food Accessibility, Energy, Education, Healthcare, Water/Waste Management, Housing, Emergency Services, Transportation Infrastructure, and Innovative Technologies.
Each relating to economic, food, health, environmental, personal, community, and political security.
Hope that helps.
Industry/Entity Type
Non Profit
Look and feel

```html
<!DOCTYPE html>
<html lang="en">
<head>
<meta charset="utf-8">
<title>Calmora Trust – Slide Templates</title>
<link href="https://fonts.googleapis.com/css2?family=Didact+Gothic&family=Questrial&display=swap" rel="stylesheet">
<style>
  :root {
    --stage: #000000;
    --slide: #ffffff;
    --brand: #1b7bc2;
    --brand-title: #1a6fb3;
    --placeholder: #5b9bd5;
    --body-text: #8a8a8a;
    --label-text: #4a4a4a;
    --icon-fill: #e3e6ea;
    --icon-mark: #2f4a66;
    --map-water: #9db8cc;
    --map-land: #d9dcd6;
  }
  * { margin: 0; padding: 0; box-sizing: border-box; }
  html, body { width: 1200px; height: 359px; overflow: hidden; background: var(--stage); }
  body { position: relative; font-family: "Didact Gothic", "Questrial", sans-serif; }

  .slide { position: absolute; top: 10px; width: 585px; height: 333px; background: var(--slide); overflow: hidden; }
  .slide--columns { left: 9px; }
  .slide--contact { left: 607px; }

  .slide__title { position: absolute; left: 19px; top: 14px; font-family: "Questrial", sans-serif; font-weight: 400; font-size: 28px; color: var(--brand-title); letter-spacing: 0.2px; line-height: 40px; }
  .slide__title-bar { position: absolute; left: 7px; top: 16px; width: 5px; height: 32px; background: var(--brand); }

  .slide__footer { position: absolute; left: 0; bottom: 0; width: 100%; height: 22px; background: var(--brand); color: #fff; font-size: 12px; line-height: 22px; }
  .footer__prev { position: absolute; left: 42px; }
  .footer__site { position: absolute; left: 0; width: 100%; text-align: center; }
  .footer__next { position: absolute; right: 42px; }
  .footer__arrow { position: absolute; top: 3px; width: 16px; height: 16px; }
  .footer__arrow--left { left: 16px; }
  .footer__arrow--right { right: 14px; }

  .column { position: absolute; top: 79px; width: 152px; }
  .column__picture { position: relative; height: 86px; background: var(--placeholder); color: #fff; font-size: 11px; display: flex; align-items: center; justify-content: center; }
  .column__shadow { height: 20px; background: radial-gradient(ellipse 50% 60% at 50% 0%, rgba(0,0,0,0.28), rgba(0,0,0,0) 100%); }
  .column__text { margin-top: 7px; font-size: 11.2px; line-height: 12.6px; color: var(--body-text); }
  .column__text p + p { margin-top: 9px; }

  .contact-list { position: absolute; left: 44px; top: 74px; list-style: none; }
  .contact-item { position: relative; padding-left: 27px; height: 38.5px; }
  .contact-item__icon { position: absolute; left: 0; top: 2px; width: 14px; height: 14px; }
  .contact-item__label { font-size: 11px; font-weight: 700; color: var(--label-text); line-height: 14px; font-family: "Questrial", sans-serif; }
  .contact-item__value { font-size: 11.5px; color: var(--body-text); line-height: 14px; }

  .map { position: absolute; left: 356px; top: 75px; width: 167px; height: 86px; background: linear-gradient(100deg, var(--map-water) 0%, var(--map-water) 38%, var(--map-land) 55%, #c9d2c4 100%); }
  .map__shadow { position: absolute; left: 356px; top: 161px; width: 167px; height: 20px; background: radial-gradient(ellipse 40% 60% at 50% 0%, rgba(0,0,0,0.28), rgba(0,0,0,0) 100%); }

  .contact-list--side { left: 363px; top: 198px; }
  .contact-list--side .contact-item { padding-left: 30px; height: 52px; }
</style>
</head>
<body>

<section class="slide slide--columns">
  <div class="slide__title-bar"></div>
  <h1 class="slide__title">Three Columns Example</h1>

  <div class="column" style="left:26px">
    <div class="column__picture">Your picture here</div>
    <div class="column__shadow"></div>
    <div class="column__text">
      <p>Stet clita kasd gubergren,no sea takimata sanctus est Lorem ipsum dolor sit amet. Consetetur labore et dolore dolores et ea rebum.</p>
      <p>Stet clita kasd gubergren, no sea takimata sanctus est Lorem ipsum dolor sit amet.</p>
    </div>
  </div>
  <div class="column" style="left:220px">
    <div class="column__picture">Your picture here</div>
    <div class="column__shadow"></div>
    <div class="column__text">
      <p>Stet clita kasd gubergren,no sea takimata sanctus est Lorem ipsum dolor sit amet. Consetetur labore et dolore dolores et ea rebum.</p>
      <p>Stet clita kasd gubergren, no sea takimata sanctus est Lorem ipsum dolor sit amet.</p>
    </div>
  </div>
  <div class="column" style="left:413px; top:81px">
    <div class="column__picture" style="height:84px">Your picture here</div>
    <div class="column__shadow"></div>
    <div class="column__text">
      <p>Stet clita kasd gubergren,no sea takimata sanctus est Lorem ipsum dolor sit amet. Consetetur labore et dolore dolores et ea rebum.</p>
      <p>Stet clita kasd gubergren, no sea takimata sanctus est Lorem ipsum dolor sit amet.</p>
    </div>
  </div>

  <footer class="slide__footer">
    <svg class="footer__arrow footer__arrow--left" viewBox="0 0 16 16"><circle cx="8" cy="8" r="7" fill="none" stroke="#fff" stroke-width="1.3"/><path d="M9.5 4.5 6 8l3.5 3.5" fill="none" stroke="#fff" stroke-width="1.6"/></svg>
    <span class="footer__prev">One Column and Table</span>
    <span class="footer__site">www.yourwebsite.com</span>
    <span class="footer__next">Contact Page</span>
    <svg class="footer__arrow footer__arrow--right" viewBox="0 0 16 16"><circle cx="8" cy="8" r="7" fill="none" stroke="#fff" stroke-width="1.3"/><path d="M6.5 4.5 10 8l-3.5 3.5" fill="none" stroke="#fff" stroke-width="1.6"/></svg>
  </footer>
</section>

<section class="slide slide--contact">
  <div class="slide__title-bar"></div>
  <h1 class="slide__title">Contact page</h1>

  <ul class="contact-list">
    <li class="contact-item">
      <svg class="contact-item__icon" viewBox="0 0 14 14"><circle cx="7" cy="7" r="7" fill="var(--icon-fill)"/><path d="M3.5 7 7 4l3.5 3H9.5v3h-5V7z" fill="var(--icon-mark)"/></svg>
      <div class="contact-item__label">Website</div>
      <div class="contact-item__value">company-name.com</div>
    </li>
    <li class="contact-item">
      <svg class="contact-item__icon" viewBox="0 0 14 14"><circle cx="7" cy="7" r="7" fill="var(--icon-fill)"/><text x="7" y="10" text-anchor="middle" font-size="9" font-weight="700" fill="var(--icon-mark)" font-family="sans-serif">@</text></svg>
      <div class="contact-item__label">E-Mail</div>
      <div class="contact-item__value">hello@company-name.com</div>
    </li>
    <li class="contact-item">
      <svg class="contact-item__icon" viewBox="0 0 14 14"><circle cx="7" cy="7" r="7" fill="var(--icon-fill)"/></svg>
      <div class="contact-item__label">Circlepage</div>
      <div class="contact-item__value">circlepage.com/company-name</div>
    </li>
    <li class="contact-item">
      <svg class="contact-item__icon" viewBox="0 0 14 14"><circle cx="7" cy="7" r="7" fill="var(--icon-fill)"/></svg>
      <div class="contact-item__label">Chirpline</div>
      <div class="contact-item__value">chirpline.com/company-name</div>
    </li>
    <li class="contact-item">
      <svg class="contact-item__icon" viewBox="0 0 14 14"><circle cx="7" cy="7" r="7" fill="var(--icon-fill)"/></svg>
      <div class="contact-item__label">Viewstream</div>
      <div class="contact-item__value">viewstream.com/company-name</div>
    </li>
  </ul>

  <div class="map" role="img" aria-label="Map showing the office location by the waterfront"></div>
  <div class="map__shadow"></div>

  <ul class="contact-list contact-list--side">
    <li class="contact-item">
      <svg class="contact-item__icon" viewBox="0 0 14 14"><circle cx="7" cy="7" r="7" fill="var(--icon-fill)"/><path d="M7 2.8a2.8 2.8 0 0 1 2.8 2.8C9.8 7.8 7 11.2 7 11.2S4.2 7.8 4.2 5.6A2.8 2.8 0 0 1 7 2.8z" fill="var(--icon-mark)"/><circle cx="7" cy="5.6" r="1" fill="var(--icon-fill)"/></svg>
      <div class="contact-item__label">Address</div>
      <div class="contact-item__value">Lorem Ipsum Street 122<br>State, Country</div>
    </li>
    <li class="contact-item">
      <svg class="contact-item__icon" viewBox="0 0 14 14"><circle cx="7" cy="7" r="7" fill="var(--icon-fill)"/><path d="M3 5.5c0-1 1.8-1.7 4-1.7s4 .7 4 1.7v.7H9.3v-.9H4.7v.9H3z" fill="var(--icon-mark)"/><rect x="4" y="6.6" width="6" height="3.6" rx="0.8" fill="var(--icon-mark)"/></svg>
      <div class="contact-item__label">Phone</div>
      <div class="contact-item__value">0123 4567 89</div>
    </li>
  </ul>

  <footer class="slide__footer">
    <svg class="footer__arrow footer__arrow--left" viewBox="0 0 16 16"><circle cx="8" cy="8" r="7" fill="none" stroke="#fff" stroke-width="1.3"/><path d="M9.5 4.5 6 8l3.5 3.5" fill="none" stroke="#fff" stroke-width="1.6"/></svg>
    <span class="footer__prev">Three columns Example</span>
    <span class="footer__site">www.yourwebsite.com</span>
    <span class="footer__next">Home</span>
    <svg class="footer__arrow footer__arrow--right" viewBox="0 0 16 16"><circle cx="8" cy="8" r="7" fill="none" stroke="#fff" stroke-width="1.3"/><path d="M6.5 4.5 10 8l-3.5 3.5" fill="none" stroke="#fff" stroke-width="1.6"/></svg>
  </footer>
</section>

</body>
</html>
```